Business Card for Auto Dealership - Clean, sharp and professional

Please use the maroon logo with the grey background. Need a sharp, clean and professional business card for an Auto Dealer. In the files provides there is three different logos. I have not decided which one to go with yet. Right now I am favoring the grey/silver background. I would like my contact info on there and the website as well. I feel like less is more and want something simple, clean and sharp. Thank you in advance for your tie and effort! I also need email signature, letterhead, etc after this

Target Market(s)

Car buyers

Industry/Entity Type

Automotive

Contact Information for Business Card

Dean
555-417-2386
www.BrinwoodAutoHub.example
Dean@BrinwoodAutoHub.example

Font styles to use
Serif
Sans Serif

Requirements
Must have
• Please use the maroon logo with the grey background. Business Card Details and logo from files. Please stick to the logo colors

```html
<!DOCTYPE html>
<html lang="en">
<head>
<meta charset="utf-8">
<title>Brinwood Auto Hub – Business Card</title>
<link rel="stylesheet" href="https://fonts.googleapis.com/css2?family=Roboto:wght@400;500;700&display=swap">
<style>
  :root {
    --maroon: #5a1a1c;
    --ink: #2e2e30;
    --card-grey: #eceef0;
    --mark-faint: #cbb9b7;
    --stage: #2c2e31;
    --card-white: #fbfbfb;
  }
  * { margin: 0; padding: 0; box-sizing: border-box; }
  html, body { width: 974px; height: 1200px; overflow: hidden; }
  body { font-family: "Roboto", Arial, sans-serif; color: var(--ink); background: var(--stage); }

  .card-front {
    position: relative; width: 974px; height: 554px;
    background: var(--card-grey); overflow: hidden;
  }
  .brand { position: absolute; left: 73px; top: 82px; display: flex; align-items: center; gap: 22px; }
  .brand-dot { width: 96px; height: 96px; border-radius: 50%; border: 9px solid var(--maroon); }
  .brand-name { font-weight: 700; font-size: 34px; letter-spacing: 1px; color: var(--maroon); line-height: 1; }

  .backdrop-ring {
    position: absolute; left: 650px; top: 65px; width: 426px; height: 426px;
    border-radius: 50%; border: 26px solid var(--mark-faint);
  }

  .holder-name { position: absolute; left: 82px; top: 266px; font-size: 32px; font-weight: 700; color: var(--maroon); }
  .contact-list { position: absolute; left: 80px; top: 330px; list-style: none; }
  .contact-list li { display: flex; align-items: center; height: 46.5px; font-size: 28px; color: var(--ink); }
  .contact-icon { width: 30px; height: 30px; margin-right: 24px; flex: none; }

  .stage { position: relative; width: 974px; height: 646px; }
  .card-white {
    position: absolute; left: 177px; top: 143px; width: 620px; height: 360px;
    background: var(--card-white); box-shadow: 0 10px 30px rgba(0,0,0,.35);
  }
  .card-white .brand-dot { position: absolute; left: 50px; top: 105px; width: 150px; height: 150px; border-width: 14px; }
  .card-white .brand-name { position: absolute; left: 232px; top: 112px; font-size: 28px; }
  .card-white .holder-name { left: 232px; top: 158px; font-size: 22px; }
  .card-white .contact-list { left: 230px; top: 200px; }
  .card-white .contact-list li { height: 34px; font-size: 19px; }
  .card-white .contact-icon { width: 20px; height: 20px; margin-right: 14px; }
</style>
</head>
<body>

<svg width="0" height="0" style="position:absolute">
  <defs>
    <symbol id="icon-phone" viewBox="0 0 30 30">
      <circle cx="15" cy="15" r="13" fill="none" stroke="#5a1a1c" stroke-width="2.2"/>
      <path d="M10.5 8.5c1-.6 1.9-.3 2.4.7l1 2c.4.8.1 1.6-.6 2l-.8.5c.6 1.6 1.9 2.9 3.5 3.6l.5-.8c.5-.7 1.3-.9 2.1-.5l1.9 1.1c.9.5 1.1 1.5.5 2.4-1.1 1.6-3 2-4.9 1-3.1-1.6-5.4-3.9-6.8-7-.8-1.9-.5-3.8 1.2-5z" fill="#5a1a1c"/>
    </symbol>
    <symbol id="icon-mail" viewBox="0 0 30 30">
      <circle cx="15" cy="15" r="13" fill="none" stroke="#5a1a1c" stroke-width="2.2"/>
      <rect x="8.5" y="10.5" width="13" height="9" rx="1" fill="#5a1a1c"/>
      <path d="M9 11.2l6 4.5 6-4.5" fill="none" stroke="#eceef0" stroke-width="1.3"/>
    </symbol>
    <symbol id="icon-web" viewBox="0 0 30 30">
      <circle cx="15" cy="15" r="12" fill="none" stroke="#5a1a1c" stroke-width="2.2"/>
      <ellipse cx="15" cy="15" rx="5" ry="12" fill="none" stroke="#5a1a1c" stroke-width="1.8"/>
      <path d="M3.5 11.5h23M3.5 18.5h23" stroke="#5a1a1c" stroke-width="1.8"/>
    </symbol>
  </defs>
</svg>

<section class="card-front">
  <div class="backdrop-ring"></div>
  <div class="brand">
    <div class="brand-dot"></div>
    <div class="brand-name">BRINWOOD AUTO HUB</div>
  </div>
  <h1 class="holder-name">Dean</h1>
  <ul class="contact-list">
    <li><svg class="contact-icon"><use href="#icon-phone"/></svg>555-417-2386</li>
    <li><svg class="contact-icon"><use href="#icon-mail"/></svg>Dean@BrinwoodAutoHub.example</li>
    <li><svg class="contact-icon"><use href="#icon-web"/></svg>www.BrinwoodAutoHub.example</li>
  </ul>
</section>

<section class="stage">
  <div class="card-white">
    <div class="brand-dot"></div>
    <div class="brand-name">BRINWOOD AUTO HUB</div>
    <h2 class="holder-name">Dean</h2>
    <ul class="contact-list">
      <li><svg class="contact-icon"><use href="#icon-phone"/></svg>555-417-2386</li>
      <li><svg class="contact-icon"><use href="#icon-mail"/></svg>Dean@BrinwoodAutoHub.example</li>
      <li><svg class="contact-icon"><use href="#icon-web"/></svg>www.BrinwoodAutoHub.example</li>
    </ul>
  </div>
</section>

</body>
</html>
```